Tolliver for Governor
We have chosen draft #108.
You have all done a great job and are amazing designers. I hope to work with you all again on future design projects for Tolliver For Governor.
Envelope: Move the address and URL up to just below the gold swoosh and you're missing a 't' in www.TolliverForGovernor.example On the back make the whole back white again add back in the emblem on the flap and make the It's Our Time fit across the back of the envelope in blue with a gradient.
Cards: Please see image and message.
Letterhead: Spot on!!!
We are now looking at #102, #103 and #106. Thank you to all the other designers, you've done a great job. There is still time for everyone to revise and resubmit their drafts, based on the comments we've made.
#90, Remove the email address from the letterhead and add Paid For By Tolliver For Governor on the same line as tolliverforgovernor.example, but on the far left side of page. Add address next to logo on front of envelope and lower It's Our Time on the back of the envelope. Remove the vertical It's Our Time from the two blue cards and center the logo on the blue card that should have no text.
#87, I like it. But everywhere you have tolliverforgovernor.example (except email addresses) remove it. I don't actually want the ""s around It's Our Time. It was away of telling you all what the exact text was. On the left side, the bottom two cards you could replace the URL with It's Our Time, just make the text bigger and bolder.
Envelope: I would like to see the back panel (not the flap) blue with white text saying "It's Our Time". On the front, move the address to the right side of the logo just under the gold swish. Add the URL under the address. Also, the address should be on 2 lines
P.O. Box 71832
Indianapolis, IN 46917
www.TolliverForGovernor.example
Card:
Logo-side, make the text much bigger (across the card bottom) and diffuse and spread out the white halo.
Info-side, move the phone number to it's own line above the address and move Name and title lines up to the lowest point in the gold swoosh. Try making the "tolliverforgovernor" in www.tolliverforgovernor.example blue like Jorel Drennick and capitalize the R,F and G.
Letterhead: on the same line as the phone and URL, but on the left side of the page, need "Paid For By Tolliver For Governor". Move the watermark logo up the page a little bit and add the line "It's Our Time" as light gray-ish watermark under it.
I done, please check
#80, please remove the URL from the logo-sides and insert the address on the info-side
please check private message
#45 and #43, let's lighten the background on the logo-side, remove the URL from both sides and insert the address.
#46, can we make the logo on the left side bigger, raise the name/title up more, insert the address and make the text bolder. On the logo side, lighter and more diffused. Also, please upload drafts for a letterhead and envelope.
I meant the logo-sides from #72 and #74
ALL: please include "Paid For By Tolliver For Governor" in small font at the bottom of the letterhead.
#70, this may be confusing, bare with me.
I like the info-side from #70 but; with the address added, name/title moved up and name in blue and remove the "phone" & "email" tags.
I like the logo-side but; make the white border around the logo the same size as the info-side and replace the URL with "It's Our Time" in font/style like "for Governor".
Would you be willing to add in the logo-side cards from both #71 and #74? Could you make the white border around the logos like the ones on the info-side in #70?
Also, need your drafts for an envelope and letterhead.
#13, I like the gradient on the front. Let's lighten the gradient, make the logo bigger and add some white diffusion around the logo (subtle). On the info side - like the flame in the lower corner. Raise the name and title area, make the name a little darker, remove the URL from the blue band, remove the "phone" and "email" tags, insert the full address. Maybe fill the center with a watermark of the logo? Also, would like to see some drafts for the letterhead and envelope.
Cards:
Info side- move name and title up more, put in the full address and add "It's Our Time" across the bottom in the same font style as "Tolliver".
Logo side- keep the logo transparency in the center of the logo, make the logo bigger and replace the white background with a light blue gradient (like in the images we uploaded).
Letterhead: remove all contact info except address, phone and URL. Add a "watermark" of all or part of the logo (w/ out the "Tolliver"). Also, at the bottom in the same line as the URL, but on the left side, add "Paid For By Tolliver For Governor".
Envelope: Insert the full address, move address and URL to the right of the logo (just under the gold line) on the back (not the flap) add "It's Our Time" feel free to try different colors in that area.
ALL: the card does not need to say "phone" or "email". You can use an icon if you want, but no need to spell it out. Also, only have the address, phone and URL on the letterhead.
Vandrel (#65,#64,#63,#62,#61,#60), What happened to the logo? Why is there sections (like a bar going across it) missing?
Sorry everyone, We've been on the road and unable to post more information or critiques.
Project Details:
1. This is a full stationary project (2-side business card, letterhead and envelope).
2. Front of business card should have either "It's Our Time" and the emblem from our provided logo or just the emblem. Background should be a light blue radial gradient with very light whitening behind emblem and/or text. Font for "It's Our Time" should match the fonts used for "Tolliver" in provided logo (colors either the same or white).
3. Address is:
PO Box 71832
4. Letterhead should have a watermark using all or part of the emblem from the provided logo.
5. Envelope should have a return address (PO Box from above).
6. Our campaign slogan is "It's Our Time".
7. On the business card there needs to be an area between the name/title area and the contact info.
8. Please do not fill in the transparent parts of the emblem or change it's color.
We will be picking a winner in the next 24 hours or less.
Good luck everyone :)

```html
<!DOCTYPE html>
<html lang="en">
<head>
<meta charset="utf-8">
<title>Tolliver for Governor – Business Card</title>
<link rel="stylesheet" href="https://fonts.googleapis.com/css2?family=Open+Sans:wght@300;400&family=Roboto+Slab:wght@700&display=swap">
<style>
  :root {
    --page-bg: #e9e7e3;
    --card-white: #ffffff;
    --brand-blue: #1f4fb0;
    --band-blue-light: #3d7fe0;
    --band-blue-dark: #1a3f9c;
    --back-blue-light: #4a90ec;
    --back-blue-dark: #14369a;
    --gold: #c9a24a;
    --ink-grey: #4d5563;
    --white: #ffffff;
  }
  * { box-sizing: border-box; margin: 0; padding: 0; }
  html, body { width: 1200px; height: 850px; overflow: hidden; }
  body {
    background: var(--page-bg);
    font-family: "Open Sans", sans-serif;
    position: relative;
  }
  .card {
    position: absolute;
    width: 520px;
    height: 300px;
    border-radius: 4px;
    overflow: hidden;
    box-shadow: 0 6px 18px rgba(0,0,0,0.18);
  }
  /* Info side */
  .card-info {
    left: 80px;
    top: 140px;
    background: var(--card-white);
  }
  .brand {
    position: absolute;
    left: 0;
    right: 0;
    top: 22px;
    text-align: center;
  }
  .brand-mark {
    display: block;
    margin: 0 auto 6px;
  }
  .brand-name {
    font-family: "Roboto Slab", serif;
    font-weight: 700;
    font-size: 30px;
    line-height: 1;
    color: var(--brand-blue);
  }
  .swoosh {
    position: absolute;
    left: 0;
    top: 150px;
  }
  .holder {
    position: absolute;
    left: 22px;
    top: 166px;
    color: var(--ink-grey);
    font-weight: 300;
  }
  .holder-name { font-size: 13px; color: var(--brand-blue); }
  .holder-title { font-size: 11px; margin-top: 1px; }
  .po-box {
    position: absolute;
    right: 26px;
    top: 196px;
    font-size: 11px;
    font-weight: 300;
    color: var(--ink-grey);
  }
  .contact-band {
    position: absolute;
    left: 0;
    right: 0;
    bottom: 0;
    height: 78px;
    background: linear-gradient(90deg, var(--band-blue-dark), var(--band-blue-light) 55%, var(--band-blue-dark));
    padding: 22px 0 0 22px;
    color: var(--white);
    font-size: 10.5px;
    font-weight: 300;
  }
  .contact-row { display: flex; line-height: 16px; }
  .contact-label { width: 48px; }
  /* Logo side */
  .card-logo {
    left: 600px;
    top: 410px;
    background: radial-gradient(ellipse at 50% 40%, var(--back-blue-light), var(--brand-blue) 60%, var(--back-blue-dark));
    color: var(--white);
  }
  .card-logo .brand { top: 56px; }
  .card-logo .brand-name { color: var(--white); font-size: 36px; }
  .card-url {
    position: absolute;
    left: 0;
    right: 0;
    bottom: 34px;
    text-align: center;
    font-size: 10.5px;
    font-weight: 300;
  }
</style>
</head>
<body>

<section class="card card-info" aria-label="Business card, info side">
  <div class="brand">
    <svg class="brand-mark" width="64" height="64" viewBox="0 0 64 64" aria-hidden="true">
      <circle cx="32" cy="32" r="30" fill="var(--brand-blue)"/>
    </svg>
    <div class="brand-name">Tolliver</div>
  </div>

  <svg class="swoosh" width="520" height="70" viewBox="0 0 520 70" aria-hidden="true">
    <path d="M0 62 C 160 66, 340 70, 520 20" fill="none" stroke="var(--gold)" stroke-width="2"/>
  </svg>

  <div class="holder">
    <div class="holder-name">Jorel Drennick</div>
    <div class="holder-title">Campaign Manager</div>
  </div>
  <div class="po-box">PO Box</div>

  <div class="contact-band">
    <div class="contact-row"><span class="contact-label">Phone</span><span>(317) 555-0148</span></div>
    <div class="contact-row"><span class="contact-label">Email</span><span>jdrennick@tolliverforgovernor.example</span></div>
  </div>
</section>

<section class="card card-logo" aria-label="Business card, logo side">
  <div class="brand">
    <svg class="brand-mark" width="80" height="80" viewBox="0 0 80 80" aria-hidden="true">
      <circle cx="40" cy="40" r="37" fill="var(--brand-blue)" stroke="var(--white)" stroke-width="3"/>
    </svg>
    <div class="brand-name">Tolliver</div>
  </div>
  <div class="card-url">www.tolliverforgovernor.example</div>
</section>

</body>
</html>
```